engineering and fabrication company- KelbroTek

We require a full functional and coded website design for an engineering and fabrication company in Western Australia.
I have attached capability statement with a content of this website.
I would like to have Fabrication services divided into two sections

1. Steel Fabrication
2. Plastic Fabrication

Industry/Entity Type

mining , waste water , oil and gas , engineering and design

Coding

Coded - Design and coding required

Number of Pages Required

5+ page

Colors
0054AA
0677BA
7BADD7
CADEEF
E8F1F8
0094D4
00A9DD
6FCCEA
C7EBF8
E9F6FB

Requirements
Must have
• Must look very professional

```html
<!DOCTYPE html>
<html lang="en">
<head>
<meta charset="UTF-8">
<title>KelbroTek – Design / Engineering / Fabrication</title>
<link rel="stylesheet" href="https://fonts.googleapis.com/css2?family=Arimo:wght@400;700&family=Roboto+Condensed:wght@700&display=swap">
<style>
  :root {
    --brand-blue: #0094D4;
    --brand-deep: #0054AA;
    --ink: #111111;
    --white: #ffffff;
    --photo-dark: #2b3038;
    --photo-mid: #5a6470;
    --spark: #d8832e;
  }
  * { margin: 0; padding: 0; box-sizing: border-box; }
  html, body {
    width: 1200px;
    height: 750px;
    overflow: hidden;
    background: var(--white);
    font-family: "Arimo", Arial, sans-serif;
  }
  .page {
    position: relative;
    width: 1200px;
    height: 750px;
  }
  .site-header {
    position: absolute;
    top: 0; left: 0;
    width: 1200px;
    height: 94px;
    background: var(--white);
    z-index: 2;
  }
  .brand {
    position: absolute;
    left: 72px;
    top: 28px;
    display: flex;
    align-items: center;
    gap: 12px;
  }
  .brand-square {
    width: 30px;
    height: 30px;
    background: var(--brand-blue);
  }
  .brand-name {
    font-family: "Arimo", Arial, sans-serif;
    font-weight: 700;
    font-size: 30px;
    color: var(--brand-blue);
    letter-spacing: 0.5px;
  }
  .main-nav {
    position: absolute;
    right: 62px;
    top: 34px;
    display: flex;
    gap: 35px;
  }
  .main-nav a {
    font-family: "Roboto Condensed", "Arial Narrow", sans-serif;
    font-weight: 700;
    font-size: 16px;
    color: var(--ink);
    text-decoration: none;
  }
  .hero {
    position: absolute;
    top: 94px;
    left: 0;
    width: 1200px;
    height: 610px;
  }
  .hero-photo {
    position: absolute;
    inset: 0;
    background:
      radial-gradient(ellipse 420px 300px at 420px 360px, rgba(216,131,46,0.45), transparent 70%),
      radial-gradient(ellipse 380px 260px at 880px 180px, rgba(216,131,46,0.35), transparent 70%),
      linear-gradient(100deg, var(--photo-dark) 0%, var(--photo-mid) 45%, #8c96a2 70%, var(--photo-dark) 100%);
  }
  .hero-title {
    position: absolute;
    top: 222px;
    left: 0;
    width: 100%;
    text-align: center;
    font-family: "Arimo", Arial, sans-serif;
    font-weight: 700;
    font-size: 37px;
    line-height: 46px;
    color: var(--white);
    text-shadow: 0 1px 3px rgba(0,0,0,0.5);
  }
  .site-footer {
    position: absolute;
    bottom: 0; left: 0;
    width: 1200px;
    height: 46px;
    background: var(--white);
    display: flex;
    align-items: center;
    justify-content: center;
  }
  .copyright {
    font-family: "Arimo", Arial, sans-serif;
    font-weight: 700;
    font-size: 12px;
    color: var(--ink);
  }
</style>
</head>
<body>
<div class="page">
  <header class="site-header">
    <div class="brand">
      <span class="brand-square"></span>
      <span class="brand-name">KelbroTek</span>
    </div>
    <nav class="main-nav">
      <a href="#">HOME</a>
      <a href="#">ABOUT</a>
      <a href="#">SERVICES</a>
      <a href="#">CONTACT</a>
    </nav>
  </header>

  <section class="hero">
    <div class="hero-photo" role="img" aria-label="Worker grinding steel with bright orange sparks flying"></div>
    <h1 class="hero-title">KelbroTek, is a multi-disciplinary design/engineering<br>and fabrication company based in Harlow Point, Kestrel Coast</h1>
  </section>

  <footer class="site-footer">
    <p class="copyright">COPYRIGHT 2022 KELBROTEK</p>
  </footer>
</div>
</body>
</html>
```